Cover and back of brochure

Our company sells all kind of filters. Now we are planning to create an image brochure for our company. This brochure should represent our high quality standard, our competence and the trust of the clients in our company.

In the attachment I added covers of other catalogs which we like. Furthermore I added nice pictures in the attachment which were downloaded from glimmerdock. In the first place we downloaded these pictures in a small size, so that several examples can be created. After we decide which picture looks best on the cover, we will buy it in a higher resolution.

More information you find in the added pdf document.

Industry/Entity Type

It Company

Colors

Designer to choose colors to be used in the design.

```html
<!DOCTYPE html>
<html lang="de">
<head>
<meta charset="utf-8">
<title>FILTRA - HAGEN e.K. – Rückseite</title>
<link rel="stylesheet" href="https://fonts.googleapis.com/css2?family=Sorts+Mill+Goudy&display=swap">
<style>
  :root {
    --brand-green: #219100;
    --paper-white: #ffffff;
  }
  * { margin: 0; padding: 0; box-sizing: border-box; }
  html, body {
    width: 1200px;
    height: 848px;
    overflow: hidden;
    background: var(--brand-green);
  }
  .back-cover {
    position: relative;
    width: 1200px;
    height: 848px;
    background: var(--brand-green);
    color: var(--paper-white);
    font-family: "Sorts Mill Goudy", "Goudy Old Style", serif;
  }
  .values {
    position: absolute;
    top: 126px;
    left: 0;
    width: 1200px;
    text-align: center;
    list-style: none;
  }
  .values__item {
    font-size: 36px;
    line-height: 48px;
    letter-spacing: 0.5px;
  }
  .values__separator {
    font-size: 24px;
    line-height: 71px;
    height: 71px;
  }
  .contact-rule {
    position: absolute;
    top: 675px;
    width: 1px;
    height: 123px;
    background: var(--paper-white);
  }
  .contact-rule--left { left: 37px; }
  .contact-rule--middle { left: 597px; }
  .contact-rule--right { left: 1163px; }
  .contact-block {
    position: absolute;
    top: 676px;
    font-size: 21px;
    line-height: 31px;
    font-style: normal;
  }
  .contact-block--address { left: 73px; }
  .contact-block--reach { left: 635px; }
</style>
</head>
<body>
  <main class="back-cover">
    <ul class="values">
      <li class="values__item">KOMPETENT</li>
      <li class="values__separator">.</li>
      <li class="values__item">HILFSBEREIT</li>
      <li class="values__separator">.</li>
      <li class="values__item">FREUNDLICH</li>
    </ul>

    <span class="contact-rule contact-rule--left"></span>
    <span class="contact-rule contact-rule--middle"></span>
    <span class="contact-rule contact-rule--right"></span>

    <address class="contact-block contact-block--address">
      FILTRA - HAGEN e.K.<br>
      Inhaber Konrad Wehlig<br>
      Lindenauer Str. 12<br>
      12305 Berlin
    </address>

    <address class="contact-block contact-block--reach">
      Tel: 030 / 555 0142<br>
      Fax: 030 / 555 0143<br>
      E-Mail: info@filtra-hagen.de<br>
      Web: www.filtra-hagen.de
    </address>
  </main>
</body>
</html>
```